New Website Footer for a Supercar dealership.

I'm looking to get a newly designed footer created for our website www.velmorcarhouse.com - one version for Desktop and 1 trimmed down version for mobile. We have one in place at the moment but I want to start it from scratch and create something far better. I know what I want to include and I have a rough design to work from which I have included in the uploaded files and I am just looking for someone to give it a high end luxury design.

If you see the sketch I've done - it must include the following links
- CURRENT STOCK
- SELL YOUR CAR
- PREVIOUSLY SOLD
Ideally use the same font that we have on our website in the top navigation

Secondary Links (in lower case)
- Delivery & Shipping
- Privacy Policy
- Modern Slavery Statement
- Luxury Cars
- Contact Us

I want also want to include
- Opening Hours
- Widget for Ratewell
- Widget for Praisly Reviews
- 4 images for awards we have won (I have included in uploaded files)
- Mailing List Sign Up
- Our company logo and address
- Quorin Finance logo (partner)
- Cookie Policy and Site Map links.
- Social Media icons

You do not have to stick to the layout of my design - feel free to change it about. I am open to colour but it needs to stay subtle and ideally working within Greyscale.

I am looking to have a black background but has a textured element to it. I was thinking along the lines of carbon fibre effect or even better would be a "Forged carbon fibre" effect in the background - I have included a screenshot of what ford carbon fibre looks like.

Target Market(s)

Luxury high end buyers

Industry/Entity Type

Automotive

Number of Pages Required

1 page

Font styles to use
Serif
Sans Serif

Colors

Designer to choose only greyscale colors for use in the design.

Requirements
Must have
• 1 Version for Desktop
1 Version for Mobile

```html
<!DOCTYPE html>
<html lang="en">
<head>
<meta charset="utf-8">
<title>Velmor Car House – Footer</title>
<link rel="stylesheet" href="https://fonts.googleapis.com/css2?family=Nunito+Sans:wght@400;600;700;800;900&display=swap">
<style>
  :root{
    --bg-dark:#121212;
    --bg-mid:#1f1f1f;
    --band:#0c0c0c;
    --text:#ffffff;
    --muted:#d6d6d6;
    --line:#9a9a9a;
    --tile:#050505;
    --accent:#e0201b;
    --paper:#ffffff;
    --ink:#1a1a1a;
  }
  *{box-sizing:border-box;margin:0;padding:0}
  html,body{width:1200px;height:847px;overflow:hidden;background:var(--bg-dark)}
  body{position:relative;font-family:"Nunito Sans",sans-serif;color:var(--text)}
  .abs{position:absolute}
  .texture{left:0;top:0;width:1200px;height:738px;
    background:radial-gradient(ellipse at 30% 40%,#262626 0%,var(--bg-mid) 40%,var(--bg-dark) 100%)}
  .band{left:0;top:738px;width:1200px;height:109px;
    background:linear-gradient(180deg,#111 0%,var(--band) 100%)}

  .main-links{left:83px;top:56px;list-style:none}
  .main-links li{display:flex;align-items:center;height:30.5px;font-weight:800;font-size:19px;letter-spacing:.2px}
  .main-links li::before{content:"";width:6px;height:6px;border:1px solid var(--muted);margin-right:12px}

  .sub-links{left:79px;top:182px;list-style:none}
  .sub-links li{height:24px;font-size:17px;line-height:24px;letter-spacing:.3px}

  .hours{left:75px;top:353px;width:318px;height:304px;border:1px solid var(--line)}
  .hours h3{position:absolute;left:22px;top:22px;font-size:15px;font-weight:800}
  .hours table{position:absolute;left:21px;top:91px;width:276px;border-collapse:collapse;font-size:13.5px}
  .hours td{height:24.7px}
  .hours td:first-child{font-weight:700}
  .hours td:last-child{text-align:right}

  .mailing{left:440px;top:52px;width:320px}
  .mailing h3{font-size:15px;font-weight:800}
  .mailing p{margin-top:5px;font-size:12px;line-height:15px;color:var(--muted)}
  .signup{left:438px;top:120px;width:319px;height:40px;border:1px solid var(--muted)}
  .signup span{position:absolute;left:16px;top:11px;font-size:11.5px}
  .signup .btn{position:absolute;left:221px;top:5px;width:92px;height:29px;border:1px solid var(--muted);
    background:var(--tile);font-size:11.5px;display:flex;align-items:center;justify-content:center}

  .award{width:152px;height:152px;background:var(--tile);display:flex;align-items:center;justify-content:center}
  .award .seal{width:96px;height:96px;border-radius:50%;background:#2a2a2a;border:1px solid #444}

  .reviews{left:441px;top:515px;width:318px;height:141px;background:var(--tile)}
  .reviews .row{position:absolute;left:0;width:318px;height:50px}
  .reviews .brand{position:absolute;left:20px;top:0;font-size:13px;font-weight:700}
  .reviews .stars{position:absolute;left:20px;top:22px;font-size:14px;letter-spacing:2px;color:var(--muted)}
  .reviews .divider{position:absolute;left:161px;top:6px;width:1px;height:40px;background:#555}
  .reviews .verdict{position:absolute;left:190px;top:13px;font-size:17px;font-weight:800;letter-spacing:2px}

  .wordmark{left:812px;top:48px;width:318px;text-align:center}
  .wordmark .name{font-size:52px;font-weight:600;letter-spacing:5px;line-height:56px}
  .wordmark .sub{font-size:22px;font-weight:600;letter-spacing:13px;margin-top:14px}

  .head{font-size:15px;font-weight:800;display:flex;align-items:center;gap:7px}
  .address-head{left:812px;top:196px}
  .partners-head{left:974px;top:196px}
  .address{left:811px;top:233px;font-size:14px;line-height:21.3px}
  .direction{left:810px;top:328px;width:92px;height:26px;border:1px solid var(--muted);font-size:12px;
    display:flex;align-items:center;justify-content:center}
  .partner{left:969px;width:161px;height:59px;display:flex;align-items:center;justify-content:center;
    font-size:14px;font-weight:700;text-align:center;line-height:16px}
  .partner.red{top:236px;background:var(--accent);color:var(--paper)}
  .partner.white{top:296px;background:var(--paper);color:var(--ink)}

  .follow{left:874px;top:439px;width:200px;text-align:center;font-size:13px}
  .social{left:816px;top:498px;width:316px;display:flex;justify-content:space-between;list-style:none}
  .social li{display:flex;align-items:center;gap:4px;font-size:11.5px;font-weight:700}
  .social li::before{content:"";width:7px;height:7px;background:var(--text)}

  .legal{left:883px;top:604px;display:flex;align-items:center;gap:12px;font-size:13px}
  .legal i{width:5px;height:5px;background:var(--accent)}

  .copyright{left:0;top:780px;width:1200px;text-align:center;font-size:15px}
</style>
</head>
<body>
  <div class="abs texture" role="img" aria-label="Forged carbon fibre texture background"></div>
  <div class="abs band"></div>

  <ul class="abs main-links">
    <li>CURRENT STOCK</li>
    <li>SELL YOUR CAR</li>
    <li>PREVIOUSLY SOLD</li>
  </ul>

  <ul class="abs sub-links">
    <li>Delivery &amp; Shipping</li>
    <li>Privacy Policy</li>
    <li>Modern Slavery Statement</li>
    <li>Luxury Cars</li>
    <li>Contact Us</li>
  </ul>

  <section class="abs hours">
    <h3>OPENNING HOURS</h3>
    <table>
      <tr><td>Monday</td><td>8:30am-6:00pm</td></tr>
      <tr><td>Tuesday</td><td>8:30am-6:00pm</td></tr>
      <tr><td>Wednesday</td><td>8:30am-6:00pm</td></tr>
      <tr><td>Thursday</td><td>8:30am-6:00pm</td></tr>
      <tr><td>Friday</td><td>8:30am-6:00pm</td></tr>
      <tr><td>Saturday</td><td>9:00am-5:00pm</td></tr>
      <tr><td>Sunday</td><td>By Appointment Only</td></tr>
    </table>
  </section>

  <div class="abs mailing">
    <h3>SIGN UP TO OUR MAILING LIST</h3>
    <p>for event invitation, exclusive previewsm, latest stock &amp; special offers</p>
  </div>
  <div class="abs signup">
    <span>Enter your email address</span>
    <div class="btn">Subscribe</div>
  </div>

  <div class="abs award" style="left:441px;top:189px"><div class="seal" role="img" aria-label="Dealer award badge"></div></div>
  <div class="abs award" style="left:605px;top:189px"><div class="seal" role="img" aria-label="Companies to inspire badge"></div></div>
  <div class="abs award" style="left:441px;top:353px"><div class="seal" role="img" aria-label="Fastest growing companies badge"></div></div>
  <div class="abs award" style="left:606px;top:353px"><div class="seal" role="img" aria-label="Social media dealer award badge"></div></div>

  <div class="abs reviews">
    <div class="row" style="top:15px">
      <div class="brand">Praisly Reviews 5.0</div>
      <div class="stars">★★★★★</div>
      <div class="divider"></div>
      <div class="verdict">EXCELENT</div>
    </div>
    <div class="row" style="top:85px">
      <div class="brand">Ratewell</div>
      <div class="stars">★★★★★</div>
      <div class="divider"></div>
      <div class="verdict">EXCELENT</div>
    </div>
  </div>

  <div class="abs wordmark">
    <div class="name">VELMOR</div>
    <div class="sub">CAR HOUSE</div>
  </div>

  <div class="abs head address-head">
    <svg width="20" height="24" viewBox="0 0 20 24" fill="none" stroke="#cfcfcf" stroke-width="1.5"><path d="M10 23s8-8 8-13a8 8 0 0 0-16 0c0 5 8 13 8 13z"/><circle cx="10" cy="10" r="3.5"/></svg>
    ADDRESS
  </div>
  <div class="abs head partners-head">
    <svg width="18" height="24" viewBox="0 0 18 24" fill="none" stroke="#cfcfcf" stroke-width="1.5"><path d="M2 1h14v22l-7-6-7 6z"/></svg>
    PARTNERS
  </div>
  <address class="abs address" style="font-style:normal">
    Harrow Lane<br>Eastmere<br>Surrey<br>RH9 4QT
  </address>
  <div class="abs direction">Direction</div>
  <div class="abs partner red">Castellan<br>Consumer Finance</div>
  <div class="abs partner white">Quorin Finance</div>

  <div class="abs follow">FOLLOW US</div>
  <ul class="abs social">
    <li>Lumo</li><li>Parla</li><li>Flit</li><li>Reelo</li><li>Vesta</li>
  </ul>

  <div class="abs legal"><span>Cookie Policy</span><i></i><span>Sitemap</span></div>

  <div class="abs copyright">© Copyright 2020 VELMOR CAR HOUSE. All Rights Reserved</div>
</body>
</html>
```